We would like to incorporate our logo into letterhead design and envelopes. We are looking for something that is moderately conservative but not old law firm style. Both the envelopes and the letterhead must have both firm addresses. We would like to incorporate the color of the logo, but only a small amount of color - perhaps on one of the borders. The addresses for the firm locations are listed below. Given that it is a law firm, it needs to somewhat conservative, but not the old school, small black font on cream colored paper design.

The firm addresses are:

27815 N. Harlow Pemberton Pkwy.
Ste 4200
Scottsdale, AZ 85391

6100 W. Cedar Avenue
Ste 700
Burbank, CA 91623

Industry/Entity Type

Legal

Colors

Designer to choose colors to be used in the design.

Requirements
Must have
• Both addresses:
• 27815 N. Harlow Pemberton Pkwy.
• Ste 4200
• Scottsdale, AZ 85391
• 6100 W. Cedar Avenue
• Ste 700
• Burbank, CA 91623
Nice to have
• Small amount of color on border(s) that matches the logo but not too much color

```html
<!DOCTYPE html>
<html lang="en">
<head>
<meta charset="utf-8">
<title>Meridale Law – Envelope</title>
<link rel="stylesheet" href="https://fonts.googleapis.com/css2?family=Marcellus&family=Lato:wght@400&display=swap">
<style>
  :root {
    --navy: #272262;
    --paper: #ffffff;
    --backdrop: #e6e6e8;
    --window: #d9d9db;
    --window-edge: #c4c4c6;
    --ink: #2b2b2b;
    --rule: #4a4a6a;
  }
  * { margin: 0; padding: 0; box-sizing: border-box; }
  html, body {
    width: 1200px; height: 1200px; overflow: hidden;
    background: var(--backdrop);
  }
  .canvas { position: relative; width: 1200px; height: 1200px; }

  .envelope {
    position: absolute; left: 179px; width: 843px; height: 436px;
    background: var(--paper); overflow: hidden;
  }
  .envelope--front { top: 131px; }
  .envelope--back { top: 634px; height: 434px; }

  .front-band {
    position: absolute; left: 291px; top: 0; width: 272px; height: 79px;
    background: var(--navy);
    display: flex; align-items: center; justify-content: center;
  }
  .front-band .firm-name { color: var(--paper); font-size: 33px; }
  .front-tab {
    position: absolute; left: 291px; bottom: 0; width: 272px; height: 13px;
    background: var(--navy);
  }
  .address-window {
    position: absolute; left: 400px; top: 215px; width: 368px; height: 162px;
    border-radius: 12px;
    background: linear-gradient(160deg, #e2e2e4 0%, #cfcfd1 40%, #ececee 60%, #d4d4d6 100%);
    border: 2px solid var(--window-edge);
  }

  .firm-name {
    font-family: "Marcellus", serif; font-weight: 400;
    letter-spacing: 0.5px; white-space: nowrap; line-height: 1;
  }

  .flap { position: absolute; left: 0; top: 0; width: 843px; height: 157px; }

  .return-block {
    position: absolute; left: 152px; top: 319px;
    display: flex; align-items: center;
  }
  .return-block .firm-name { color: var(--navy); font-size: 34px; padding-right: 8px; }
  .divider { width: 1px; height: 75px; background: var(--navy); margin-right: 11px; }
  .addresses {
    font-family: "Lato", sans-serif; font-size: 13.5px; color: var(--ink);
    line-height: 20px;
  }
  .addresses .condensed { font-size: 12.5px; letter-spacing: -0.6px; }
  .base-rule {
    position: absolute; left: 56px; top: 407px; width: 730px; height: 1px;
    background: var(--rule);
  }
</style>
</head>
<body>
<main class="canvas">
  <section class="envelope envelope--front" aria-label="Envelope front">
    <div class="front-band"><span class="firm-name">MERIDALE LAW</span></div>
    <div class="address-window"></div>
    <div class="front-tab"></div>
  </section>

  <section class="envelope envelope--back" aria-label="Envelope back">
    <svg class="flap" viewBox="0 0 843 157" aria-hidden="true">
      <path d="M0 0 H843 L808 112 Q790 152 748 156 H92 Q55 152 38 112 Z" fill="var(--navy)"/>
    </svg>
    <div class="return-block">
      <span class="firm-name">MERIDALE LAW</span>
      <span class="divider"></span>
      <address class="addresses" style="font-style:normal">
        <div>6100 W. Cedar Avenue, Ste 700, Burbank, CA 91623</div>
        <div class="condensed">27815 N. Harlow Pemberton Pkwy. Ste 4200, Scottsdale, AZ 85391</div>
      </address>
    </div>
    <div class="base-rule"></div>
  </section>
</main>
</body>
</html>
```